Dietetic office: Bright Plate

I want to give my business card a modern and warm look (which attracts the eye and has a reassuring side), which links dietetics to a moment of well-being. The front and back sides must be used (not just to put the logo on the front side)

The map should be eye-catching and easy to read. I don't necessarily want to have a plain background, which I find visually weighs down the maps.
I really like the square format of a business card with rounded edges which is different from what we are used to finding (and why not take this square diagonally?), however I am not closed to another format as long as I like the style.

Who am I? Mireille, 32 years old, Dietician and passionate about food since always. I am specialized in slimming and an expert in micro nutrition, which means that I take into account not only the nutritional balance while maintaining pleasure (if foods are present in the business card, I do not want some cliché things where there would just be fruits and vegetables, but really something more global), but also the psycho-emotional dimension that I will treat with food supplements based on plants, fruits or vegetables.

-----------------------------------------------------------------------------------

 Mention to appear on the card IN FRENCH (please be careful in case of translation that the use of words is correct):

Mireille DORAN
Dietician Nutritionist
Expert in Slimming and Micro-Nutrition

Slogan: I help you lose weight sustainably with pleasure and by reconciling your events

Catchphrases: Want to lose weight? Do you like going out? Do you have a lot of events? And is pleasure on your plate important to you?

Make an appointment on Rendiplan or on 06 41 58 30 92
mireille.brightplate@exemplo-mail.fr
Address: Health Center, Rue des Glycines, 13127 Vitrolles
www.brightplate-exemple.fr
Friendwall + Picturo Logo

- The company logo has been uploaded for your viewing. Other file formats can be made available if required.
- I would like a place for a photo of me to be possible.

Good morning,
I want to have a business card that is both lively and warm. Which will easily catch the eye while being easy to read and make people understand that I am in the field of well-being.
I like the square side in business cards (and why not use them diagonally?), or a more classic but original one.
Both the front and back sides must be used (I don't want to have the logo on just one side)
I don't want to have a plain background, but rather something more muted (I really like the suggestion from "Reed Cloud Graphic Designer" for this)
the use of logo for telephone, mail, address, rendiplan, friendwall, pictu etc is possible in order to facilitate reading

Please follow the various elements of the brief regarding the text and use the French text as it is.

I like business cards preferably square (with the possibility of using them diagonally).
The map should be eye-catching and easy to read.
It must bring pep while having softness which brings back to the well-being side
The card must be used on the front and back for the different elements (I do not want to have only the logo on the front side)
The text must correspond to the brief (be careful with the translation which can sometimes be bad)
I don't want to have a plain blue or orange background. I really like the idea of the background from "Reed Cloud Graphic Designer"

You can if you wish use symbols for contacts, telephone, rendiplan, address, fw, pictu....

Target Market(s)

mainly women between 25 and 65 years old + men around 40 years old

Contact Information for Business Card

Font styles to use
Sans Serif
Script

Colors
0054AA
0677BA
7BADD7
CADEEF
E8F1F8
0094D4
00A9DD
6FCCEA
C7EBF8
E9F6FB
00AB8E
00BBA5
67D7C9
C6EFE9
E9F9F6
FFC000
F8CF3A
FAE287
FDF2CF
FEFAEE
F0912C
F2A743
F7CA91
FBE8D2
FDF5EE

Requirements
Must have
• some pep! while being refined
Nice to have
• I really like the square format of a business card with rounded edges which is different from what we are used to finding, however I am not closed to another format as long as I like the style.
Should not have
• if foods are represented, only show fruits and vegetables (too cliché)

```html
<!DOCTYPE html>
<html lang="fr">
<head>
<meta charset="utf-8">
<title>Bright Plate – Carte de visite</title>
<link href="https://fonts.googleapis.com/css2?family=Anton&family=Oswald:wght@500;600;700&display=swap" rel="stylesheet">
<style>
  :root {
    --bg: #ebebeb;
    --white-strip: #f0f0f0;
    --orange-light: #ebae4c;
    --orange-mid: #e9a443;
    --orange-deep: #cf621f;
    --orange-band: #d06b25;
    --blue-pill: #3f92cf;
    --blue-text: #1f5ca6;
    --blue-logo: #3a8dc4;
    --teal: #3a99ac;
    --teal-light: #6ccad8;
    --back-grey: #e2e2e2;
    --photo-light: #f2f2f2;
    --photo-dark: #2d2d2d;
  }
  * { box-sizing: border-box; margin: 0; padding: 0; }
  html, body { width: 1200px; height: 960px; overflow: hidden; }
  body {
    background: var(--bg);
    font-family: "Oswald", "Arial Narrow", sans-serif;
    position: relative;
  }

  .card {
    position: absolute;
    top: 230px;
    width: 500px;
    height: 500px;
    border-radius: 58px;
    overflow: hidden;
    box-shadow: 0 18px 40px rgba(0,0,0,0.12);
  }

  /* Front */
  .card-front { left: 70px; background: var(--white-strip); }
  .brand-strip {
    position: absolute; left: 0; top: 0; width: 112px; height: 100%;
    display: flex; align-items: center; justify-content: center;
  }
  .brand-name {
    transform: rotate(-90deg);
    white-space: nowrap;
    font-weight: 600;
    font-size: 38px;
    color: var(--blue-logo);
    display: flex; align-items: center; gap: 12px;
  }
  .brand-dot {
    width: 16px; height: 16px; border-radius: 50%;
    background: var(--orange-mid);
  }
  .front-panel {
    position: absolute; left: 112px; top: 0; right: 0; bottom: 0;
    border-radius: 44px 0 0 44px;
    background: radial-gradient(circle at 100% 100%, var(--orange-deep) 0%, var(--orange-mid) 32%, var(--orange-light) 70%);
    color: #fff;
  }
  .name-first {
    position: absolute; top: 28px; left: 0; right: 0; text-align: center;
    font-family: "Anton", sans-serif; font-size: 46px; line-height: 1; letter-spacing: -0.5px;
  }
  .name-last {
    position: absolute; top: 78px; left: 0; right: 0; text-align: center;
    font-family: "Anton", sans-serif; font-size: 100px; line-height: 1; letter-spacing: -2px;
  }
  .title-pill {
    position: absolute; top: 196px; left: 50%; transform: translateX(-50%);
    background: var(--blue-pill); border-radius: 8px;
    padding: 3px 12px; white-space: nowrap;
    font-weight: 600; font-size: 18px; letter-spacing: -0.2px;
  }
  .photo-slot {
    position: absolute; top: 238px; left: 50%; transform: translateX(-50%);
    width: 212px; height: 212px; border-radius: 50%;
    background: linear-gradient(180deg, var(--photo-light) 0%, #d9d9d9 100%);
  }
  .accent-dot {
    position: absolute; width: 38px; height: 38px; border-radius: 50%;
    background: var(--teal-light);
  }
  .accent-top { top: 258px; right: 42px; }
  .accent-bottom { top: 400px; left: 52px; }
  .expertise {
    position: absolute; bottom: 26px; left: 0; right: 0; text-align: center;
    font-weight: 500; font-size: 14px;
  }

  /* Back */
  .card-back { left: 630px; background: var(--back-grey); }
  .corner-disc {
    position: absolute; top: -48px; left: -48px;
    width: 112px; height: 112px; border-radius: 50%; background: var(--teal);
  }
  .back-content {
    position: absolute; top: 44px; left: 26px; width: 344px;
    text-align: center; color: var(--blue-text); font-weight: 700;
  }
  .slogan { font-size: 13px; line-height: 1.3; font-weight: 600; }
  .booking { margin-top: 14px; font-size: 19px; line-height: 1.2; }
  .booking small { display: block; font-size: 13px; }
  .contact-line { margin-top: 18px; font-size: 18px; line-height: 1.25; }
  .contact-line.email { font-size: 16px; }
  .socials {
    margin-top: 16px; display: flex; justify-content: center; gap: 18px;
    font-size: 14px; font-weight: 600;
  }
  .social-item { display: flex; align-items: center; gap: 6px; }
  .social-item::before {
    content: ""; width: 12px; height: 12px; border-radius: 50%; background: var(--blue-text);
  }
  .bottom-disc {
    position: absolute; bottom: 22px; left: 170px;
    width: 68px; height: 68px; border-radius: 50%; background: var(--teal);
  }
  .catch-band {
    position: absolute; top: 0; right: 0; width: 112px; height: 100%;
    background: var(--orange-band);
    border-radius: 44px 0 0 44px;
    display: flex; align-items: center; justify-content: center;
  }
  .catchphrase {
    writing-mode: vertical-rl;
    color: #fdf2e6;
    font-weight: 700; font-size: 17px; line-height: 1.25;
    height: 420px; text-align: center;
  }
</style>
</head>
<body>

<section class="card card-front" aria-label="Recto de la carte">
  <div class="brand-strip">
    <div class="brand-name"><span class="brand-dot"></span>Bright Plate</div>
  </div>
  <div class="front-panel">
    <div class="name-first">MIREILLE</div>
    <div class="name-last">DORAN</div>
    <div class="title-pill">DIÉTÉTICIENNE NUTRITIONNISTE</div>
    <div class="photo-slot" role="img" aria-label="Emplacement pour la photo portrait de la diététicienne"></div>
    <div class="accent-dot accent-top" role="img" aria-label="Pastille décorative avec un pilon de volaille"></div>
    <div class="accent-dot accent-bottom" role="img" aria-label="Pastille décorative avec un morceau de fromage"></div>
    <div class="expertise">Experte en Amincissement et en Micro-Nutrition</div>
  </div>
</section>

<section class="card card-back" aria-label="Verso de la carte">
  <div class="corner-disc" role="img" aria-label="Pastille décorative avec un morceau de fromage"></div>
  <div class="back-content">
    <p class="slogan">Je vous aide à mincir durablement avec plaisir et<br>en conciliant vos évènements!</p>
    <p class="booking">Prise de rendez-vous sur Rendiplan<small>ou au</small></p>
    <p class="contact-line">06 41 58 30 92</p>
    <p class="contact-line email">mireille.brightplate@exemplo-mail.fr</p>
    <p class="contact-line">Pôle Bien-Être, Rue des Glycines,<br>13590 Valmerette</p>
    <p class="contact-line">www.brightplate-exemple.fr</p>
    <div class="socials">
      <span class="social-item">Friendwall</span>
      <span class="social-item">Picturo</span>
    </div>
  </div>
  <div class="bottom-disc" role="img" aria-label="Pastille décorative avec un pilon de volaille"></div>
  <div class="catch-band">
    <p class="catchphrase">Envie de mincir ? Vous aimez sortir ? Vous avez beaucoup d'évènements ? Et le plaisir dans votre assiette est important pour vous ?</p>
  </div>
</section>

</body>
</html>
```